Teilnehmerzertifikat für Expeditionsmobil
Zielgruppe
Wir bitten alles Rund um das Thema Expeditionsmobil an. Unter anderem unsere Lagerfeuer und Weite Fahrt nach Tunesien und dafür benötige ich ein Teilnehmer Zertifikat.
Aufgabenstellung
Im Hintergrund soll ein Bild von der Sahara verarbeitet sein und im Vordergrund möchte ich von jedem Teilnehmer ein Bild mit dem eigenen Expeditonsfahrzeug einfügen. Das Zertifikat soll persöhnlich und wie von einem Freund sein

```html
<!DOCTYPE html>
<html lang="de">
<head>
<meta charset="utf-8">
<title>Teilnehmerzertifikat</title>
<link href="https://fonts.googleapis.com/css2?family=Montserrat:wght@700;800&family=Ubuntu:wght@400;500&display=swap" rel="stylesheet">
<style>
  :root {
    --sand: #d4b87b;
    --orange: #d4843a;
    --white: #ffffff;
    --brown: #4a2e16;
    --label: #8a5a2c;
    --red: #e3242b;
  }
  html, body { margin: 0; padding: 0; overflow: hidden; }
  body { width: 849px; height: 1200px; background: var(--sand); }
  .certificate {
    position: relative; width: 849px; height: 1200px; overflow: hidden;
    background: var(--sand); font-family: "Ubuntu", sans-serif;
  }
  .backdrop { position: absolute; inset: 0; }
  .first-name {
    position: absolute; left: 58px; top: 48px; margin: 0;
    font-family: "Montserrat", sans-serif; font-weight: 800;
    font-size: 104px; line-height: 1; color: var(--orange); letter-spacing: 1px;
  }
  .last-name {
    position: absolute; left: 60px; top: 160px; margin: 0;
    font-family: "Montserrat", sans-serif; font-weight: 800;
    font-size: 78px; line-height: 1; color: var(--white); letter-spacing: 2px;
  }
  .photo-label {
    position: absolute; left: 700px; top: 296px; margin: 0;
    font-family: "Montserrat", sans-serif; font-weight: 700; font-size: 28px; color: #111;
  }
  .message {
    position: absolute; left: 53px; top: 740px; margin: 0; width: 700px;
    font-size: 21px; line-height: 29.5px; color: var(--brown); letter-spacing: 1.6px;
  }
  .place-date {
    position: absolute; left: 55px; top: 1055px; margin: 0;
    font-size: 15px; font-weight: 500; color: var(--label); letter-spacing: 0.5px;
  }
  .signature-line { position: absolute; left: 452px; width: 178px; height: 0; border-top: 1.5px solid var(--brown); }
  .signature-line.place { top: 1077px; }
  .signature-line.sign { top: 1140px; }
  .organizer {
    position: absolute; left: 676px; top: 1030px; width: 130px; margin: 0;
    font-family: "Montserrat", sans-serif; font-weight: 800; font-size: 19px;
    line-height: 1.05; color: var(--red); text-transform: uppercase;
  }
  .dots { position: absolute; left: 0; top: 1100px; }
</style>
</head>
<body>
<main class="certificate">
  <svg class="backdrop" width="849" height="1200" viewBox="0 0 849 1200">
    <defs>
      <linearGradient id="desertTones" x1="0" y1="0" x2="0" y2="1">
        <stop offset="0" stop-color="#9fb9d3"/>
        <stop offset="0.28" stop-color="#d8d2c4"/>
        <stop offset="0.36" stop-color="#c9a374"/>
        <stop offset="0.7" stop-color="#b88c5c"/>
        <stop offset="1" stop-color="#c79a66"/>
      </linearGradient>
    </defs>
    <path role="img" aria-label="Foto: Konvoi von Expeditionsmobilen auf einer Sandpiste durch die tunesische Wüste"
          d="M0 0 H449 C600 40 760 120 849 190 V610 C760 740 660 805 560 805 C330 805 130 690 0 540 Z"
          fill="url(#desertTones)"/>
    <line x1="0" y1="26" x2="849" y2="26" stroke="var(--white)" stroke-width="4"/>
    <g fill="none" stroke="var(--white)" stroke-width="2.5">
      <path d="M0 300 C200 240 430 220 640 250"/>
      <path d="M0 312 C200 254 430 234 640 263"/>
      <path d="M0 324 C200 268 430 248 640 276"/>
      <path d="M0 336 C200 282 430 262 640 289"/>
      <path d="M0 348 C200 296 430 276 640 302"/>
      <path d="M610 410 C700 400 780 420 849 440"/>
      <path d="M620 425 C710 415 785 435 849 455"/>
      <path d="M630 440 C715 430 790 450 849 470"/>
    </g>
    <g fill="none" stroke="var(--white)" stroke-width="3">
      <path d="M630 165 L849 232"/>
      <path d="M640 180 L849 245"/>
      <path d="M612 180 L596 330"/>
    </g>
    <polygon points="632,192 849,256 849,430 590,378" fill="var(--white)"/>
  </svg>

  <h1 class="first-name">Vorname</h1>
  <h2 class="last-name">Nachname</h2>
  <p class="photo-label">Foto</p>

  <p class="message">Ihr habt mit<br>Begeisterung und<br>Abenteuerlust an unserer<br>gemeinsamen Reise durch Tunesien teilgenommen.<br>Mit eurem Expeditionsmobil habt ihr die Wüste<br>bezwungen, neue Freundschaften geschlossen und die<br>Magie dieses einzigartigen Landes erlebt.<br>Danke, dass ihr Teil dieser besonderen Tour wart –<br>auf viele weitere Abenteuer!</p>

  <p class="place-date">Ort und Datum</p>
  <div class="signature-line place"></div>
  <div class="signature-line sign"></div>

  <p class="organizer">Lagerfeuer und Weite Fahrt 2024</p>

  <svg class="dots" width="160" height="100" viewBox="0 0 160 100" aria-hidden="true">
    <g fill="var(--white)" opacity="0.85">
      <circle cx="7" cy="18" r="10"/><circle cx="78" cy="18" r="10"/><circle cx="145" cy="18" r="10"/>
      <circle cx="7" cy="89" r="10"/><circle cx="78" cy="89" r="10"/>
    </g>
  </svg>
</main>
</body>
</html>
```